Redesign of Proposal Document

looking to redesign this proposal document to fit the colours and styles of my company as well as make it read easily, grab the reader and look professional.

my website is www.brindlecoatpainting.com.au
facebook and instagram @brindlecoatpainting

```html
<!DOCTYPE html>
<html lang="en">
<head>
<meta charset="utf-8">
<title>Brindlecoat Painting – Success Stories</title>
<link rel="stylesheet" href="https://fonts.googleapis.com/css2?family=Roboto+Slab:wght@300;400;700;800&family=Crimson+Pro:wght@500&display=swap">
<style>
  :root {
    --brand: #00557a;
    --ink: #231f20;
    --panel: #ecf1f3;
    --white: #ffffff;
    --photo-a: #6f9bb3;
    --photo-b: #2f6686;
  }
  * { margin: 0; padding: 0; box-sizing: border-box; }
  html, body { width: 848px; height: 1200px; overflow: hidden; background: var(--white); }
  .page {
    position: relative;
    width: 848px; height: 1200px;
    background: var(--white);
    border: 18px solid var(--brand);
    overflow: hidden;
  }
  .frame-lines { position: absolute; left: -18px; top: -18px; width: 848px; height: 1200px; pointer-events: none; }
  .brand {
    position: absolute; left: 0; right: 0; top: 38px;
    display: flex; flex-direction: column; align-items: center;
  }
  .brand-mark { width: 150px; height: 150px; border: 6px solid var(--brand); }
  .brand-name {
    margin-top: 14px;
    font-family: "Crimson Pro", serif; font-weight: 500;
    font-size: 27px; color: var(--brand); letter-spacing: -0.2px;
  }
  .title-bar {
    position: absolute; left: 86px; top: 253px; width: 637px; height: 88px;
    background: var(--brand); border-radius: 9px;
    display: flex; align-items: center; justify-content: center;
  }
  .title-bar h1 {
    font-family: "Roboto Slab", serif; font-weight: 800;
    font-size: 58px; color: var(--white); letter-spacing: 1.5px;
  }
  .story {
    position: absolute; left: 71px; top: 389px; width: 460px;
    font-family: "Roboto Slab", serif; font-weight: 300;
    font-size: 16.6px; line-height: 29.3px; color: var(--ink);
  }
  .outcomes {
    position: absolute; left: 548px; top: 373px; width: 264px; height: 439px;
    background: var(--panel); padding: 10px 13px 0 14px;
  }
  .outcomes h2 {
    font-family: "Roboto Slab", serif; font-weight: 700;
    font-size: 23.5px; color: var(--brand); letter-spacing: 0.6px;
    margin-bottom: 18px;
  }
  .outcomes ul { list-style: none; }
  .outcomes li {
    font-family: "Roboto Slab", serif; font-weight: 300;
    font-size: 16px; line-height: 23.5px; color: var(--ink);
    padding: 0 0 13px 3px; margin-bottom: 12px;
    border-bottom: 2px solid var(--brand);
  }
  .outcomes li:last-child { border-bottom: none; }
  .hallway-photo {
    position: absolute; left: 53px; top: 873px; width: 759px; height: 291px;
    background: linear-gradient(100deg, var(--photo-a) 0%, #8fb5c8 40%, var(--photo-b) 100%);
  }
</style>
</head>
<body>
<div class="page">
  <svg class="frame-lines" viewBox="0 0 848 1200" aria-hidden="true">
    <polyline points="776,18 776,316 741,316" fill="none" stroke="#00557a" stroke-width="7"/>
    <polyline points="104,322 67,322 67,1182" fill="none" stroke="#00557a" stroke-width="7"/>
  </svg>

  <header class="brand">
    <div class="brand-mark"></div>
    <div class="brand-name">Brindlecoat Painting</div>
  </header>

  <div class="title-bar"><h1>Success Stories</h1></div>

  <p class="story">Recently Marcus was approached by an existing client, as her daughter was in the process of purchasing a property, and wasn't happy with the existing colours. Marcus was able to visit the property with the client while they were in contractual negotations to provide a quote for painting services.<br>During his quote, he identified existing damage to the ceiling, which he was able to quote to repair as well. The quote and the project scope was finalised before handover, and Marcus and his team were able to complete the repairs and paintwork in the first few weeks of ownership. They worked together with the clients to arrange to paint one half of the house while the clients occupied the other half, to minimise disruption to their living.</p>

  <aside class="outcomes">
    <h2>Project outcomes</h2>
    <ul>
      <li>The customer's house looked like new.</li>
      <li>The customer's 'new home' experience was enhanced.</li>
      <li>The customer now has a trusted painter to rely upon for future works.</li>
      <li>The customer was so happy with the progress and quality outcomes.</li>
    </ul>
  </aside>

  <div class="hallway-photo" role="img" aria-label="Freshly painted hallway with staircase, sideboard and framed artwork, looking through to a living room"></div>
</div>
</body>
</html>
```